Need Catering Menu designed - design that we want is attached

Hi,
We need a new catering menu designed for our cafe.
I have attached our coffee menu, we would like it to follow the same kind of layout.
It needs to be A4, and can be double sided.
I have attached a word doc of our catering menu, so this is what needs to be on the catering menu you produce.
Also, our contact details need to be on both sides of the menu:
Visit us instore to discuss catering options, or call 0438 672 914 or email marla@tevrostudio.com.au
I have also attached our new logo which I'd like incorporated into the menu
Target Market(s)
Doctors/Nurses
Hospital staff
University Students
Industry/Entity Type
Catering
Look and feel

```html
<!DOCTYPE html>
<html lang="en">
<head>
<meta charset="utf-8">
<title>Ward Rounds – Catering Menu</title>
<link rel="stylesheet" href="https://fonts.googleapis.com/css2?family=Josefin+Sans:wght@400&display=swap">
<style>
  :root {
    --bg: #3f3436;
    --cream: #fcf5a6;
    --white: #ffffff;
    --ink: #3f3436;
  }
  * { margin: 0; padding: 0; box-sizing: border-box; }
  html, body { width: 1200px; height: 848px; overflow: hidden; background: var(--bg); }
  body { font-family: "Josefin Sans", sans-serif; }
  .menu { position: relative; width: 1200px; height: 848px; background: var(--bg); }

  .brand {
    position: absolute; left: 40px; top: 48px; width: 175px; height: 154px;
    background: var(--cream); display: flex; align-items: center; justify-content: center;
  }
  .brand-name {
    color: var(--ink); font-size: 22px; letter-spacing: 2px; text-align: center; line-height: 1.25;
    text-transform: uppercase;
  }

  .heading {
    position: absolute; left: 252px; top: 70px; width: 340px;
    display: flex; align-items: center; gap: 12px; color: var(--white);
  }
  .heading-rule { flex: 1; height: 7px; border-top: 2px solid var(--white); border-bottom: 2px solid var(--white); }
  .heading-text { font-size: 27px; white-space: nowrap; padding-top: 4px; }

  .contact {
    position: absolute; left: 230px; top: 135px; width: 390px;
    color: var(--white); font-size: 16.5px; line-height: 22px; text-align: center;
  }

  .panel { position: absolute; border: 2px solid var(--cream); }
  .panel-title {
    position: absolute; border: 2px solid var(--cream); background: var(--bg);
    color: var(--cream); font-size: 32px; letter-spacing: 8px;
    display: flex; align-items: center; justify-content: center; padding-top: 6px;
  }
  .panel-body {
    position: absolute; color: var(--cream); font-size: 18.5px; line-height: 25.6px; white-space: nowrap;
  }
  .price-line { display: flex; align-items: baseline; }
  .leader { flex: 1; border-bottom: 2px dotted var(--cream); margin: 0 2px 5px; }
  .gap { height: 25.6px; }

  .panel-left { left: 42px; top: 292px; width: 507px; height: 527px; }
  .title-left { left: 119px; top: 261px; width: 357px; height: 62px; }
  .body-left { left: 72px; top: 340px; width: 450px; }

  .panel-right { left: 598px; top: 52px; width: 563px; height: 773px; }
  .title-right { left: 676px; top: 21px; width: 411px; height: 64px; }
  .body-right { left: 628px; top: 98px; width: 502px; }
</style>
</head>
<body>
<main class="menu">
  <div class="brand"><span class="brand-name">Ward<br>Rounds</span></div>

  <header class="heading">
    <span class="heading-rule"></span>
    <h1 class="heading-text" style="font-weight:400">CATERING MENU</h1>
    <span class="heading-rule"></span>
  </header>

  <p class="contact">Visit us instore to discuss catering options,<br>or call: 0438 672 914<br>email: marla@tevrostudio.com.au</p>

  <section class="panel panel-left"></section>
  <h2 class="panel-title title-left" style="font-weight:400">LUNCH</h2>
  <div class="panel-body body-left">
    <div class="price-line"><span>Foccacias</span><span class="leader"></span><span>$8.50</span></div>
    <div>Cut in half – please let us know if you want them<br>toasted</div>
    <div>**Same options as wraps and sandwiches – Plus:</div>
    <div>-Roast Veggie: butter, pesto, grilled eggplant,<br>grilled zucchini, roasted capsicum, feta cheese,<br>baby spinach</div>
    <div>-Salami: butter, pesto, baby spinach, mild salami,<br>roasted capsicum, olives, feta cheese</div>
    <div>-Chicken Schnitzel: Butter, Housemade coleslaw,<br>chicken schnitzel</div>
    <div class="gap"></div>
    <div class="price-line"><span>Bagels</span><span class="leader"></span><span>$9.0</span></div>
    <div>Turkey: butter, cranberry sauce, baby spinach,<br>tomato, camembert cheese</div>
    <div>Smoked Salmon: butter, cream cheese, baby<br>spinach, tomato, smoked salmon</div>
  </div>

  <section class="panel panel-right"></section>
  <h2 class="panel-title title-right" style="font-weight:400">LUNCH</h2>
  <div class="panel-body body-right">
    <div class="price-line"><span>Sandwiches&nbsp; or Wraps</span><span class="leader"></span><span>$7.50</span></div>
    <div>Sandwiches cut into quarters – Wraps cut into thirds</div>
    <div>-Ham: butter, pickle spread, cheese, tomato, champagne<br>leg ham</div>
    <div>-Turkey: butter, cranberry sauce, lettuce mix, tomato,<br>turkey breast</div>
    <div>-Sweet Chilli Chicken:&nbsp; butter, sweet chilli sauce, aioli,<br>lettuce mix, tomato, cheese, sweet chilli chicken tenders</div>
    <div>-Chicken Schnitzel: butter, aioli, lettuce mix, tomato, tasty<br>cheese, chicken schnitzel</div>
    <div>-Chicken and Avocado: butter, aioli, lettuce mix, tomato,<br>cheese, chicken breast, avocado</div>
    <div>-Egg: butter, lettuce mix, egg, aioli, parsley, spring onion</div>
    <div>-Tuna: butter, lettuce, tuna, aioli, sundried tomato, spring<br>onion</div>
    <div>-B.L.T.: butter, aioli, lettuce, tomato, bacon</div>
    <div>-Salad: butter, lettuce mix, red onion, cucumber, capsicum,<br>tomato, avocado, tasty cheese</div>
    <div>-Tandoori Chicken: butter, tzatziki, lettuce mix, tomato,<br>tandoori chicken</div>
    <div>-Waldorf Chicken: butter, cos lettuce, chicken, seeded<br>mustard, celery, walnuts, aioli</div>
    <div>-Chicken Ceasar: butter, aioli, cos lettuce, chicken,<br>parmesan cheese, bacon</div>
    <div>-Cajun Chicken: butter, lettuce mix, tomato, red onion,<br>Cajun chicken</div>
    <div>-Barbeque Chicken: butter, BBQ,</div>
    <div>-Felafel:</div>
  </div>
</main>
</body>
</html>
```